New Zealand Export company needs business cards

We need new business cards to match our new logo for a company based in New Zealand who deal specifically with the Pacific Islands. We source, consolidate and ship products out of New Zealand to the Pacific Islands. Will attach our old ones and also new logo.
Would like the Islands we deal with and the areas of work we have access to, to be included on the business cards.

Contact Information for Business Card

T +64 9 571 3048
F +64 9 571 6285
12-18 Kowhai Lane, Drury, 2113
PO Box 814, Drury, Auckland 2247, New Zealand
www.falconfreight.example.nz
E sales@falconfreight.example.nz

Font styles to use
Sans Serif

Colors
85abd2
33a6d7
ffffff

Requirements
Must have
• A company of PWM

```html
<!DOCTYPE html>
<html lang="en">
<head>
<meta charset="utf-8">
<title>Falcon Freight – Business Card</title>
<link rel="stylesheet" href="https://fonts.googleapis.com/css2?family=Arimo:wght@400;700&family=Open+Sans:wght@400&display=swap">
<style>
  :root {
    --backdrop: #fecb98;
    --card-white: #ffffff;
    --charcoal: #231f20;
    --navy: #004f73;
    --teal: #0b8f86;
    --address-blue: #4bb4e0;
    --brand-blue: #1a5aa6;
    --tagline: #0f4a6e;
    --contact-blue: #1f58a8;
    --icon-top: #3b7cc2;
    --icon-bottom: #1c5e58;
  }
  * { margin: 0; padding: 0; box-sizing: border-box; }
  html, body {
    width: 1200px; height: 1000px; overflow: hidden;
    background: var(--backdrop);
  }
  .business-card {
    position: absolute; left: 68px; top: 150px;
    width: 1050px; height: 600px;
    background: var(--card-white);
    overflow: hidden;
    box-shadow: 8px 8px 10px rgba(60, 40, 20, 0.45);
    font-family: "Arimo", Arial, sans-serif;
  }
  .card-artwork { position: absolute; inset: 0; }
  .pin-icon { position: absolute; left: 75px; top: 165px; width: 50px; height: 50px; }
  .address {
    position: absolute; left: 68px;
    color: var(--address-blue);
    font-size: 24px; line-height: 30px;
  }
  .address--street { top: 252px; }
  .address--postal { top: 342px; }
  .brand {
    position: absolute; left: 560px; top: 140px;
    display: flex; align-items: center; gap: 14px;
  }
  .brand-square { width: 34px; height: 34px; background: var(--brand-blue); }
  .brand-name {
    color: var(--brand-blue);
    font-size: 40px; font-weight: 700; letter-spacing: 1px;
    text-transform: uppercase;
  }
  .tagline {
    position: absolute; left: 638px; top: 218px;
    color: var(--tagline); font-size: 32px;
  }
  .contact-list { position: absolute; left: 560px; top: 303px; list-style: none; }
  .contact-item {
    position: relative; height: 50px; display: flex; align-items: center;
    color: var(--contact-blue);
    font-family: "Open Sans", Arial, sans-serif; font-size: 28px;
    white-space: nowrap;
  }
  .contact-item + .contact-item { margin-top: 18px; }
  .contact-item:nth-child(3) { margin-top: 22px; }
  .contact-item svg { width: 50px; height: 50px; flex: none; margin-right: 20px; }
  .contact-item--email { font-size: 26px; }
  .contact-item--web { font-family: "Arimo", Arial, sans-serif; font-size: 26px; }
</style>
</head>
<body>
<div class="business-card">
  <svg class="card-artwork" viewBox="0 0 1050 600" role="img" aria-label="Decorative flowing wave artwork in charcoal, navy, sky blue and teal">
    <defs>
      <linearGradient id="artworkTone" x1="0" y1="1" x2="1" y2="0">
        <stop offset="0" stop-color="var(--charcoal)"/>
        <stop offset="0.4" stop-color="var(--charcoal)"/>
        <stop offset="0.62" stop-color="var(--navy)"/>
        <stop offset="1" stop-color="var(--teal)"/>
      </linearGradient>
    </defs>
    <path d="M0 0 H1050 V60 L540 45 L470 255 L219 600 H0 Z" fill="url(#artworkTone)"/>
  </svg>

  <svg class="pin-icon" viewBox="0 0 50 50" aria-hidden="true">
    <rect width="50" height="50" rx="9" fill="var(--icon-top)"/>
    <path d="M0 32 H50 V41 a9 9 0 0 1 -9 9 H9 a9 9 0 0 1 -9 -9 Z" fill="var(--icon-bottom)"/>
    <path d="M25 8 a11 11 0 0 1 11 11 c0 9 -11 23 -11 23 s-11 -14 -11 -23 a11 11 0 0 1 11 -11 Z" fill="#fff"/>
    <circle cx="25" cy="19" r="5" fill="var(--icon-top)"/>
  </svg>

  <p class="address address--street">12-18 Kowhai Lane,<br>Drury, 2113</p>
  <p class="address address--postal">PO Box 814, Drury,<br>Auckland 2247,<br>New Zealand</p>

  <div class="brand">
    <span class="brand-square"></span>
    <span class="brand-name">Falcon Freight</span>
  </div>
  <p class="tagline">A company of PWM</p>

  <ul class="contact-list">
    <li class="contact-item">
      <svg viewBox="0 0 50 50" aria-hidden="true">
        <rect width="50" height="50" rx="9" fill="var(--icon-top)"/>
        <path d="M0 34 H50 V41 a9 9 0 0 1 -9 9 H9 a9 9 0 0 1 -9 -9 Z" fill="var(--icon-bottom)"/>
        <path d="M15 14 l5 -2 l4 8 l-3 3 c2 4 5 7 8 8 l3 -3 l8 4 l-2 5 c-12 2 -25 -11 -23 -23 Z" fill="#fff"/>
        <path d="M28 12 a10 10 0 0 1 10 10 M28 17 a5 5 0 0 1 5 5" stroke="#fff" stroke-width="2.2" fill="none"/>
      </svg>
      +64 9 571 3048
    </li>
    <li class="contact-item">
      <svg viewBox="0 0 50 50" aria-hidden="true">
        <rect width="50" height="50" rx="9" fill="var(--icon-top)"/>
        <path d="M0 34 H50 V41 a9 9 0 0 1 -9 9 H9 a9 9 0 0 1 -9 -9 Z" fill="var(--icon-bottom)"/>
        <rect x="9" y="16" width="8" height="24" rx="2" fill="#fff"/>
        <rect x="19" y="8" width="16" height="12" fill="#fff"/>
        <rect x="18" y="20" width="24" height="20" rx="2" fill="#fff"/>
        <g fill="var(--icon-top)">
          <rect x="22" y="24" width="4" height="3"/><rect x="28" y="24" width="4" height="3"/><rect x="34" y="24" width="4" height="3"/>
          <rect x="22" y="30" width="4" height="3"/><rect x="28" y="30" width="4" height="3"/><rect x="34" y="30" width="4" height="3"/>
        </g>
      </svg>
      Fax: +64 9 571 6285
    </li>
    <li class="contact-item contact-item--email">
      <svg viewBox="0 0 50 50" aria-hidden="true">
        <rect width="50" height="50" rx="9" fill="var(--icon-top)"/>
        <path d="M0 34 H50 V41 a9 9 0 0 1 -9 9 H9 a9 9 0 0 1 -9 -9 Z" fill="var(--icon-bottom)"/>
        <path d="M10 22 L25 12 L40 22 V40 H10 Z" fill="#fff"/>
        <rect x="15" y="14" width="20" height="16" fill="#fff" stroke="var(--icon-top)" stroke-width="1.5"/>
        <text x="25" y="26" text-anchor="middle" font-size="11" font-family="Arial, sans-serif" fill="var(--icon-top)">@</text>
        <path d="M10 22 L25 33 L40 22 M10 40 L22 30 M40 40 L28 30" stroke="var(--icon-top)" stroke-width="1.5" fill="none"/>
      </svg>
      sales@falconfreight.example.nz
    </li>
    <li class="contact-item contact-item--web">
      <svg viewBox="0 0 50 50" aria-hidden="true">
        <rect width="50" height="50" rx="9" fill="var(--icon-top)"/>
        <path d="M0 34 H50 V41 a9 9 0 0 1 -9 9 H9 a9 9 0 0 1 -9 -9 Z" fill="var(--icon-bottom)"/>
        <g stroke="#fff" stroke-width="2.2" fill="none">
          <circle cx="25" cy="25" r="15"/>
          <ellipse cx="25" cy="25" rx="6" ry="15"/>
          <path d="M10 25 H40 M13 17 H37 M13 33 H37"/>
        </g>
      </svg>
      www.falconfreight.example.nz
    </li>
  </ul>
</div>
</body>
</html>
```